Emergency Medical Training and Events Company Business Needs Business Card Design

We are in need of a business card for our dynamic company expanding its customer base and need to be easily contacted and identified for when we visit with government officials, potential EMS / Fire agencies and county coordinators to arrange for training programs for first responders to better prepare them for critical thinking at critical incidents.

Target Market(s)

EMS/Fire and Event Promoters

Industry/Entity Type

Medical

Contact Information for Business Card

Two cards, comparable designs:

Martin K. Halvey, Principal, m.halvey@rvqtlo.com
Owen Tash, Event and Training Specialist, o.tash@rvqtlo.com

Font styles to use
Other font styles liked:
• Cambria

Colors

Designer to choose colors to be used in the design.

Requirements
Must have
• Company Logo, Spots for Name, Title, Phone Number, Email, Website
• A bullet list stating that we offer, QRB CPR and First Aid Instructors, Hold the Line Instructors, Event EMS, CME's, MCI Training and Planning. We prefer to have a black background for the card but if you can make a blue or white card stand out we would review that as well.
Should not have
• Tacky logos or special sayings ... simple, elegant, professional is the look we seek

```html
<!DOCTYPE html>
<html lang="en">
<head>
<meta charset="utf-8">
<title>RVQ Solutions – Business Card</title>
<link rel="stylesheet" href="https://fonts.googleapis.com/css2?family=Poppins:wght@400;500;600;700&display=swap">
<style>
  :root {
    --navy: #0b1a4e;
    --navy-deep: #09184a;
    --red: #c8191f;
    --white: #ffffff;
    --card-white: #fbfbfb;
    --backdrop: #e6e3de;
    --text-navy: #14215a;
  }
  * { box-sizing: border-box; margin: 0; padding: 0; }
  html, body {
    width: 900px; height: 1200px; overflow: hidden;
    background: var(--backdrop);
    font-family: "Poppins", sans-serif;
  }
  .canvas { position: relative; width: 900px; height: 1200px; }
  .card {
    position: absolute; left: 75px; width: 768px; height: 438px;
    border-radius: 18px; overflow: hidden;
    box-shadow: 0 6px 18px rgba(0,0,0,0.25);
  }
  /* Front */
  .card-front { top: 133px; background: var(--card-white); }
  .holder-name {
    position: absolute; left: 53px; top: 64px;
    font-size: 32px; font-weight: 600; color: var(--red); letter-spacing: 0.2px;
    line-height: 44px;
  }
  .holder-title {
    position: absolute; left: 54px; top: 108px;
    font-size: 21px; font-weight: 500; color: var(--text-navy); letter-spacing: 1.6px;
  }
  .accent-dash {
    position: absolute; left: 54px; top: 169px; width: 28px; height: 3px; background: var(--red);
  }
  .contact-list { position: absolute; left: 52px; top: 220px; list-style: none; }
  .contact-item {
    display: flex; align-items: center; height: 34px;
    font-size: 22px; color: var(--text-navy);
  }
  .contact-item.group-gap { margin-top: 23px; }
  .contact-icon { width: 26px; height: 26px; margin-right: 17px; flex: none; }
  .brand-front {
    position: absolute; left: 390px; top: 40px; width: 340px; height: 360px;
    display: flex; flex-direction: column; align-items: center; justify-content: center;
  }
  .brand-mark-circle {
    width: 150px; height: 150px; border-radius: 50%; background: var(--navy); margin-bottom: 22px;
  }
  .brand-name-front { font-size: 38px; font-weight: 600; color: var(--navy); white-space: nowrap; }

  /* Back */
  .card-back { top: 627px; height: 441px; background: var(--navy-deep); }
  .brand-back {
    position: absolute; left: 80px; top: 105px; height: 136px;
    display: flex; align-items: center;
  }
  .brand-mark-back { width: 130px; height: 130px; border-radius: 50%; background: var(--white); }
  .brand-divider { width: 3px; height: 136px; background: var(--red); margin: 0 24px 0 64px; }
  .brand-name-back { font-size: 52px; font-weight: 700; color: var(--white); letter-spacing: 0.5px; white-space: nowrap; }
  .services-band {
    position: absolute; left: 0; bottom: 0; width: 100%; height: 106px;
    background: var(--red); color: var(--white);
    display: flex; align-items: center; justify-content: center; text-align: center;
    font-size: 21.5px; line-height: 30px;
  }
</style>
</head>
<body>
<main class="canvas">
  <section class="card card-front">
    <h1 class="holder-name">Martin K. Halvey</h1>
    <p class="holder-title">PRINCIPAL</p>
    <div class="accent-dash"></div>
    <ul class="contact-list">
      <li class="contact-item">
        <svg class="contact-icon" viewBox="0 0 26 26"><rect x="7" y="1.5" width="12" height="23" rx="2" fill="none" stroke="#c8191f" stroke-width="2.4"/><line x1="7" y1="19" x2="19" y2="19" stroke="#c8191f" stroke-width="1.8"/></svg>
        555 204 3817
      </li>
      <li class="contact-item">
        <svg class="contact-icon" viewBox="0 0 26 26"><path d="M2 9 Q13 1 24 9 L21 12 L18 10 L18 8 Q13 6 8 8 L8 10 L5 12 Z" fill="#c8191f"/><path d="M7 13 L19 13 L22 22 L4 22 Z" fill="#c8191f"/><circle cx="13" cy="17.5" r="2.3" fill="#fff"/></svg>
        555 731 6042
      </li>
      <li class="contact-item group-gap">
        <svg class="contact-icon" viewBox="0 0 26 26"><rect x="1.5" y="5" width="23" height="16" rx="1.5" fill="#c8191f"/><path d="M2 6 L13 14.5 L24 6" fill="none" stroke="#fff" stroke-width="1.6"/></svg>
        m.halvey@rvqtlo.com
      </li>
      <li class="contact-item">
        <svg class="contact-icon" viewBox="0 0 26 26" fill="none" stroke="#c8191f" stroke-width="1.8"><circle cx="13" cy="13" r="11"/><ellipse cx="13" cy="13" rx="5" ry="11"/><line x1="2" y1="13" x2="24" y2="13"/><path d="M4 7.5 H22 M4 18.5 H22"/></svg>
        www.rvqtlo.com
      </li>
    </ul>
    <div class="brand-front">
      <div class="brand-mark-circle"></div>
      <div class="brand-name-front">RVQ Solutions</div>
    </div>
  </section>

  <section class="card card-back">
    <div class="brand-back">
      <div class="brand-mark-back"></div>
      <div class="brand-divider"></div>
      <div class="brand-name-back">RVQ Solutions</div>
    </div>
    <p class="services-band">QRB CPR and First Aid Instructors, Hold the Line Instructors,<br>Event EMS, CME's, MCI Training &amp; Planning</p>
  </section>
</main>
</body>
</html>
```